Design a helpdesk ticketing platform *

We are launching a helpdesk ticketing platform. Very much like quellbox.com, merrylark.com, pivolta.com, brisktray.com etc. We have a full mid-fidelity prototype built and we want someone to build the full fidelity of the product.

You can view the full mid-fidelity prototype here: https://lnk.vexora.net/Qa8Lpw

The best way moving forward is to just design the following 4 pages

- Main Dashboard https://lnk.vexora.net/81hRtd
- All tickets https://lnk.vexora.net/jwNoEb
- Viewing a ticket https://lnk.vexora.net/Ys4VmK
- Contacts https://lnk.vexora.net/pHeXuo

Target Market(s)

Small business owners

Industry/Entity Type

Saas

Number of Pages Required

4 page

Font styles to use
Serif
Sans Serif

Colors

Designer to choose colors to be used in the design.

Requirements
Must have
• Must follow the prototype exactly. We are not looking for any UX changes. We want the designe xactly as the prototype is. We are only looking for design ideas.
Should not have
• modern, clean. We'd love to see the primary color as yellow, purple, orange, green or blue. You choose which one you think looks best and go with that.

```html
<!DOCTYPE html>
<html lang="en">
<head>
<meta charset="utf-8">
<title>deskharbor – Dashboard</title>
<link href="https://fonts.googleapis.com/css2?family=Roboto:wght@300;400;500;700&display=swap" rel="stylesheet">
<style>
:root{
  --stage:#687894;
  --brand:#1e9ff2;
  --side:#454e60;
  --side-dark:#3a4252;
  --side-active:#545e71;
  --side-text:#dfe3ea;
  --side-icon:#a9b1bf;
  --content:#e9edf2;
  --head:#f3f5f8;
  --white:#ffffff;
  --ink:#2f3a4a;
  --muted:#8a93a2;
  --line:#e3e7ec;
  --link:#2a8ad0;
  --orange:#fbb534;
  --blue:#2188c9;
  --green:#a2d27f;
  --teal:#22c4cd;
  --red:#dd4b3f;
  --open:#16a34a;
}
*{box-sizing:border-box;margin:0;padding:0}
html,body{width:1200px;height:742px;overflow:hidden}
body{background:var(--stage);font-family:'Roboto',sans-serif;position:relative}
.app{position:absolute;left:78px;top:58px;width:1048px;height:599px;background:var(--content);overflow:hidden}
.sidebar{position:absolute;left:0;top:0;width:166px;height:100%;background:var(--side)}
.brand{height:61px;background:var(--brand);color:var(--white);font-weight:500;font-size:19px;letter-spacing:1px;display:flex;align-items:center;padding-left:25px}
.new-ticket{height:46px;background:var(--side-dark);color:var(--side-text);font-size:11.5px;display:flex;align-items:center;padding-left:20px;letter-spacing:.2px}
.nav{list-style:none;margin-top:2px}
.nav li{position:relative;height:37px;display:flex;align-items:center;padding-left:20px;color:var(--side-text);font-size:8.5px;font-weight:500;letter-spacing:.6px;margin-bottom:3px}
.nav li svg{width:16px;height:16px;margin-right:9px;stroke:var(--side-icon);fill:none;stroke-width:1.2}
.nav li.active{background:var(--side-active);color:var(--white);font-weight:700;font-size:7.5px}
.nav li.active::before{content:"";position:absolute;left:0;top:0;width:4px;height:100%;background:var(--brand)}
.nav li.active svg{stroke:var(--white)}
.nav .chev{position:absolute;right:14px;width:14px;height:10px;margin:0}
.nav li.gap{margin-top:5px}
.topbar{position:absolute;left:166px;top:0;right:0;height:61px;background:var(--white);border-bottom:2px solid #eef0f3}
.toggle{position:absolute;left:16px;top:20px;width:30px;height:20px}
.topbar .divider{position:absolute;left:74px;top:0;width:2px;height:61px;background:#eef0f3}
.search-icon{position:absolute;left:94px;top:24px;width:18px;height:18px}
.search-text{position:absolute;left:129px;top:26px;font-size:12.5px;color:var(--muted);font-weight:300}
.user{position:absolute;right:246px;top:26px;font-size:11px;color:var(--ink);white-space:nowrap}
.avatar{position:absolute;left:807px;top:16px;width:35px;height:35px;border-radius:50%;background:radial-gradient(circle at 50% 45%,#e7a27c,#b5673f 70%,#6d4a3a)}
.menu-dots{position:absolute;left:857px;top:22px;width:6px;height:22px}
.page-head{position:absolute;left:166px;top:61px;right:0;height:53px;background:var(--head)}
.page-head h1{position:absolute;left:14px;top:17px;font-size:16px;font-weight:500;color:var(--ink);letter-spacing:.2px}
.page-head h1 small{font-size:11px;font-weight:300;color:#6b7482;margin-left:5px;letter-spacing:0}
.stats{position:absolute;left:180px;top:135px;display:flex;gap:11px}
.stat{width:162px;height:75px;background:var(--white);display:flex;box-shadow:0 1px 2px rgba(0,0,0,.06)}
.stat .icon{width:62px;height:100%;display:flex;align-items:center;justify-content:center}
.stat .icon svg{width:40px;height:40px;fill:none;stroke:var(--white);stroke-width:2.6;stroke-linejoin:round;stroke-linecap:round}
.stat .body{flex:1;padding:23px 0 0 8px}
.stat .label{font-size:12px;font-weight:500;display:block;white-space:nowrap}
.stat .value{font-size:26px;font-weight:500;color:var(--ink);display:block;margin:2px 0 0 19px;letter-spacing:1px}
.orange .icon{background:var(--orange)} .orange .label{color:var(--orange)}
.blue .icon{background:var(--blue)} .blue .label{color:var(--blue)}
.green .icon{background:var(--green)} .green .label{color:var(--green)}
.teal .icon{background:var(--teal)} .teal .label{color:var(--teal)}
.red .icon{background:var(--red)} .red .label{color:var(--red)}
.activity{position:absolute;left:180px;top:234px;width:854px;height:370px;background:var(--white);border-top:2px solid #dde2e8}
.activity h2{font-size:18px;font-weight:400;color:var(--ink);padding:14px 0 0 9px;height:52px;border-bottom:1px solid var(--line)}
.activity table{position:absolute;left:0;top:67px;width:840px;border-collapse:collapse;font-size:11.5px;color:var(--ink)}
.activity th,.activity td{height:36.4px;border-bottom:1px solid var(--line);text-align:left;vertical-align:middle;padding-left:9px}
.activity th{font-weight:500;font-size:12.5px}
.activity th+th,.activity td+td{border-left:1px solid var(--line)}
.col-num{width:24px}
.col-title{width:402px}
.col-updated{width:345px}
.activity td.title{color:var(--link);font-size:11px}
.badge{display:inline-block;color:var(--white);font-weight:700;font-size:10.5px;padding:2px 6px;border-radius:8px;line-height:13px}
.badge.opened{background:var(--open)}
.badge.closed{background:var(--red)}
</style>
</head>
<body>
<div class="app">
  <aside class="sidebar">
    <div class="brand">deskharbor</div>
    <div class="new-ticket">NEW TICKET</div>
    <ul class="nav">
      <li class="active"><svg viewBox="0 0 16 16"><circle cx="8" cy="8" r="6.5"/><path d="M8 8l3-3M5 10h6"/></svg>DASHBOARD</li>
      <li class="gap"><svg viewBox="0 0 16 16"><path d="M2 4h7v10H2zM5 2h7l2 2v8h-2"/></svg>TICKETS<svg class="chev" viewBox="0 0 14 10"><path d="M1 2l6 6 6-6"/></svg></li>
      <li><svg viewBox="0 0 16 16"><circle cx="8" cy="5.5" r="3.5"/><path d="M2 15c0-3.5 2.7-5.5 6-5.5s6 2 6 5.5z"/></svg>CONTACTS</li>
      <li><svg viewBox="0 0 16 16"><circle cx="8" cy="8" r="2.5"/><circle cx="8" cy="8" r="6" stroke-dasharray="2 1.5"/></svg>ADMIN SETTING<svg class="chev" viewBox="0 0 14 10"><path d="M1 2l6 6 6-6"/></svg></li>
      <li><svg viewBox="0 0 16 16"><rect x="2" y="1.5" width="12" height="13"/><path d="M4.5 5h2M9.5 5h2M4.5 10l2 2M6.5 10l-2 2M9.5 11h2"/></svg>ACCOUNT &amp; BILLING</li>
    </ul>
  </aside>

  <header class="topbar">
    <svg class="toggle" viewBox="0 0 30 20"><path d="M0 10l4-3v6z" fill="var(--brand)"/><path d="M8 3h20M8 10h20M8 17h20" stroke="#c3c9d2" stroke-width="2.2"/></svg>
    <span class="divider"></span>
    <svg class="search-icon" viewBox="0 0 18 18"><circle cx="7.5" cy="7.5" r="6" fill="none" stroke="#b7bec8" stroke-width="2"/><path d="M12 12l5 5" stroke="#b7bec8" stroke-width="2.2"/></svg>
    <span class="search-text">Search for tickets,....</span>
    <span class="user">Rowan Ellery</span>
    <span class="avatar" role="img" aria-label="User profile photo"></span>
    <svg class="menu-dots" viewBox="0 0 6 22"><circle cx="3" cy="3" r="2.6" fill="#8e96a3"/><circle cx="3" cy="11" r="2.6" fill="#8e96a3"/><circle cx="3" cy="19" r="2.6" fill="#8e96a3"/></svg>
  </header>

  <div class="page-head"><h1>DASHBOARD<small>Ticket summarry</small></h1></div>

  <section class="stats">
    <div class="stat orange"><div class="icon"><svg viewBox="0 0 40 40"><path d="M4 18l20-12 3 5a3 3 0 0 0 4 3l3 5-20 12-3-5a3 3 0 0 0-4-3z"/><path d="M4 18l3 14h25l-1-8"/><path d="M22 16l1 2M25 21l1 2M28 26l1 2"/></svg></div><div class="body"><span class="label">OPEN TICKETS</span><span class="value">16</span></div></div>
    <div class="stat blue"><div class="icon"><svg viewBox="0 0 40 40"><rect x="6" y="8" width="28" height="26" rx="2"/><path d="M6 14h28M13 5v6M27 5v6M14 24l4 4 8-8"/></svg></div><div class="body"><span class="label">DUE TODAY</span><span class="value">14</span></div></div>
    <div class="stat green"><div class="icon"><svg viewBox="0 0 40 40"><path d="M4 18l20-12 3 5a3 3 0 0 0 4 3l3 5-20 12-3-5a3 3 0 0 0-4-3z"/><path d="M4 18l3 14h25l-1-8"/><path d="M22 16l1 2M25 21l1 2M28 26l1 2"/></svg></div><div class="body"><span class="label">UNASSIGNED</span><span class="value">14</span></div></div>
    <div class="stat teal"><div class="icon"><svg viewBox="0 0 40 40"><path d="M4 18l20-12 3 5a3 3 0 0 0 4 3l3 5-20 12-3-5a3 3 0 0 0-4-3z"/><path d="M4 18l3 14h25l-1-8"/><path d="M22 16l1 2M25 21l1 2M28 26l1 2"/></svg></div><div class="body"><span class="label">OVER DUE</span><span class="value">0</span></div></div>
    <div class="stat red"><div class="icon"><svg viewBox="0 0 40 40"><circle cx="20" cy="20" r="14"/><path d="M10 30l20-20"/></svg></div><div class="body"><span class="label">NOT RESOLVED</span><span class="value">11</span></div></div>
  </section>

  <section class="activity">
    <h2>Recent Activites</h2>
    <table>
      <thead><tr><th class="col-num">#</th><th class="col-title">Title</th><th class="col-updated">Updated</th><th>Status</th></tr></thead>
      <tbody>
        <tr><td>1</td><td class="title">milo Varga assigned forgot to cc, trying again (#15) to milo Varga</td><td>2018-11-03 13:18:19</td><td><span class="badge opened">Opened</span></td></tr>
        <tr><td>2</td><td class="title">milo Varga assigned forgot to cc, trying again (#15) to milo Varga</td><td>2018-11-03 11:21:56</td><td><span class="badge opened">Opened</span></td></tr>
        <tr><td>3</td><td class="title">milo Varga assigned forgot to cc, trying again (#15) to milo Varga</td><td>2018-11-03 11:03:28</td><td><span class="badge opened">Opened</span></td></tr>
        <tr><td>4</td><td class="title">milo Varga assigned forgot to cc, trying again (#15) to milo Varga</td><td>2018-11-03 09:05:55</td><td><span class="badge closed">Closed</span></td></tr>
        <tr><td>5</td><td class="title">milo Varga assigned forgot to cc, trying again (#15) to milo Varga</td><td>2018-09-16 12:37:04</td><td><span class="badge closed">Closed</span></td></tr>
      </tbody>
    </table>
  </section>
</div>
</body>
</html>
```